Calloway needs a modernized design

We would like a modern update (that can be responsive) to our existing website. Attached are the two existing pages we would like new concepts of - our home page and a page about one of our locations.

Calloway is provides executive offices and virtual office services. Startups, law firms, and financial services are our primary clients. We would like a professional, clean design, leaning towards minimalist. We intend to greatly reduce/eliminate the long paragraphs of text.

Industry/Entity Type

Business Service

Number of Pages Required

2 page

Requirements
Must have
• A design that can be responsive
Nice to have
• Large image(s) on home page that rotate.

```html
<!DOCTYPE html>
<html lang="en">
<head>
<meta charset="utf-8">
<title>Calloway Business Centers</title>
<link href="https://fonts.googleapis.com/css2?family=Jost:wght@400;500;600&display=swap" rel="stylesheet">
<style>
:root{
  --navy:#233363;
  --navy-box:#2c3d73;
  --ink:#2b3a66;
  --white:#ffffff;
  --form-bg:#e6e6e6;
  --form-text:#6a6a6a;
  --form-line:#c9c9c9;
  --button:#1a8fd6;
  --footer-text:#4a4a4a;
}
*{margin:0;padding:0;box-sizing:border-box}
html,body{width:1200px;height:2422px;overflow:hidden;background:var(--white)}
body{position:relative;font-family:"Jost",sans-serif;color:var(--ink)}
.abs{position:absolute}
.line{display:block;white-space:nowrap}

.hero-photo{left:0;top:0;width:1200px;height:549px;
  background:linear-gradient(180deg,#1e2a44 0%,#3b4660 30%,#b88758 52%,#d9965a 58%,#2a2e3a 64%,#2c3a52 80%,#1c2638 100%)}
.site-nav{left:250px;top:0;width:701px;height:94px;background:var(--white);
  box-shadow:0 6px 14px rgba(0,0,0,.3);border-radius:0 0 4px 4px}
.brand{left:18px;top:24px;display:flex;align-items:center;gap:10px;color:var(--navy);font-size:24px;font-weight:500}
.brand-dot{width:44px;height:44px;border-radius:50%;background:var(--navy)}
.nav-link{top:35px;font-size:14.5px;color:var(--navy);white-space:nowrap}
.nav-link.current{text-decoration:underline;text-underline-offset:5px}

.hero-title{left:249px;top:146px;font-size:44px;line-height:62px;font-weight:600;color:var(--white);letter-spacing:.5px}
.hero-card{left:288px;top:358px;width:367px;height:232px;background:var(--white);padding:13px 16px;
  font-size:13.6px;line-height:17.5px;color:var(--ink);box-shadow:0 8px 16px rgba(0,0,0,.2)}
.offer-box{left:670px;top:358px;width:281px;height:96px;background:var(--navy-box);color:var(--white)}
.offer-col{top:10px;font-size:7px;line-height:8.5px;font-weight:600;text-transform:uppercase}
.offer-col p{margin-bottom:8px}
.offer-divider{left:178px;top:0;width:1px;height:96px;background:rgba(255,255,255,.3)}
.offer-col.location{text-transform:none;font-weight:400}
.offer-col.location h4{font-size:10px;font-weight:600;text-transform:uppercase;margin-bottom:2px}

.intro-heading{left:0;top:627px;width:1200px;text-align:center;font-size:26px;line-height:38px;font-weight:400;color:var(--navy)}
.intro-text{top:767px;text-align:center;font-size:13.6px;line-height:19.7px}
.intro-left{left:255px;width:376px}
.intro-right{left:620px;width:325px}

.services-photo{left:0;top:963px;width:1200px;height:450px;
  background:linear-gradient(100deg,#1a1716 0%,#2a2420 35%,#5a4e42 60%,#7d7365 80%,#4d463e 100%)}
.services-title{left:285px;top:1083px;font-size:44px;line-height:60px;font-weight:600;color:var(--white);letter-spacing:.5px}
.services-text{left:249px;top:1160px;font-size:14px;line-height:21.7px;color:var(--white)}

.play-box{top:1445px;width:60px;height:33px;background:var(--navy);display:flex;align-items:center;justify-content:center}
.video-copy{top:1442px;font-size:13px;line-height:19px;color:var(--navy)}
.video-copy strong{display:block;font-weight:600;font-size:14px}

.closing-text{left:300px;top:1557px;width:600px;text-align:center;font-size:18.5px;line-height:26px;color:var(--navy)}

.form-band{left:0;top:1747px;width:1200px;height:675px;background:var(--form-bg)}
.form-title{left:0;top:1796px;width:1200px;text-align:center;font-size:17px;font-weight:400;color:#555}
.field{height:40px;padding-top:2px;border-bottom:1px solid var(--form-line);font-size:16.5px;color:var(--form-text)}
.field.left{left:309px;width:281px}
.field.right{left:607px;width:283px;text-align:right}
.submit-btn{left:567px;top:2266px;width:60px;height:29px;background:var(--button);color:var(--white);
  font-size:10px;display:flex;align-items:center;justify-content:center;border-radius:2px}

.footer-legal{left:291px;top:2340px;font-size:13px;font-weight:600;color:var(--footer-text);line-height:33px;letter-spacing:.5px}
.footer-link{top:2360px;font-size:14px;color:var(--footer-text)}
</style>
</head>
<body>

<div class="abs hero-photo" role="img" aria-label="City skyline across the water at sunset"></div>

<header class="abs site-nav">
  <div class="abs brand"><span class="brand-dot"></span>Calloway</div>
</header>
<nav>
  <span class="abs nav-link current" style="left:502px">Home</span>
  <span class="abs nav-link" style="left:571px">Properties</span>
  <span class="abs nav-link" style="left:655px">Virtual Tours</span>
  <span class="abs nav-link" style="left:751px">Gallery</span>
  <span class="abs nav-link" style="left:823px">Broker Referrals</span>
</nav>

<h1 class="abs hero-title">EXECUTIVE OFFICE<br>SOLUTIONS. ONE LOW<br>COST.</h1>

<div class="abs hero-card">
  <span class="line">Value is found in our flexibility and comprehensive</span>
  <span class="line">service offerings. Starting or growing a business is</span>
  <span class="line">difficult enough and renting your office, virtual</span>
  <span class="line">office or meeting room shouldn't be. We can help</span>
  <span class="line">you scale your space as quickly as needed,</span>
  <span class="line">depending upon your requirement. Start with an</span>
  <span class="line">ondemand office or meeting room and as your</span>
  <span class="line">business scales, grow into a virtual office and then</span>
  <span class="line">a Full Service office.</span>
</div>

<div class="abs offer-box">
  <div class="abs offer-col" style="left:7px"><p>Executive<br>Offices Suites</p><p>On-Demand<br>Meeting Rooms</p></div>
  <div class="abs offer-col" style="left:81px"><p>On-Demand<br>Training Rooms</p><p>Virtual Office<br>Solutions</p><p>Video Conference<br>Solutions</p></div>
  <div class="abs offer-divider"></div>
  <div class="abs offer-col location" style="left:189px"><h4>Location</h4>2480 Harlow Ave.<br>Suite 410<br>Dallas, Texas 75201</div>
</div>

<h2 class="abs intro-heading">Building companies &amp; communities<br>to share &amp; collaborate ideas</h2>
<p class="abs intro-text intro-left">
  <span class="line">Companies that partner with Calloway share more</span>
  <span class="line">than a prestigious address. They also share ideas</span>
  <span class="line">&amp; services. Our Executive Office Busines Centers</span>
  <span class="line">are places where savy, growing companies can</span>
  <span class="line">network, interact &amp; learn from one another.</span>
</p>
<p class="abs intro-text intro-right">
  <span class="line">We are also a large part of the community within</span>
  <span class="line">our home state of Texas. We have been a</span>
  <span class="line">contributing business memeber for 15 years, and</span>
  <span class="line">are proud to say we have build a solid reputation</span>
  <span class="line">as an upstanding member of the Dallas, Ft. Worth</span>
  <span class="line">&amp; Houston business communities.</span>
</p>

<div class="abs services-photo" role="img" aria-label="Hands typing on a laptop at a wooden desk beside a potted succulent"></div>
<h2 class="abs services-title">OUR SERVICES</h2>
<p class="abs services-text">
  <span class="line">The service we provide in terms of technology</span>
  <span class="line">is unparalleled in our industry. We outfit each</span>
  <span class="line">of our locations with 100Mbps of bandwidth!</span>
  <span class="line">We have the latest systems in place, with all</span>
  <span class="line">locations offering IP PBX telephone systems,</span>
  <span class="line">Vantor IP telephones and RingAhead Technology</span>
  <span class="line">including Voicemail to Email and Efax, with</span>
  <span class="line">local technical support. All of this is in place to</span>
  <span class="line">ensure you can operate your business</span>
  <span class="line">with maximum efficiency.</span>
</p>

<div class="abs play-box" style="left:309px"><svg width="10" height="12" viewBox="0 0 10 12"><path d="M0 0L10 6L0 12Z" fill="#fff"/></svg></div>
<div class="abs video-copy" style="left:379px"><strong>INFORMATION VIDEO</strong>Calloway Full Executive<br>Office Suites</div>
<div class="abs play-box" style="left:670px"><svg width="10" height="12" viewBox="0 0 10 12"><path d="M0 0L10 6L0 12Z" fill="#fff"/></svg></div>
<div class="abs video-copy" style="left:739px"><strong>INFORMATION VIDEO</strong>Calloway Virtual Office<br>Services</div>

<p class="abs closing-text">
  <span class="line">Our customers begin their road to profitability with</span>
  <span class="line">Calloway and stay for extended terms. Our customers</span>
  <span class="line">know that we will manage every aspect of the</span>
  <span class="line">workplace, so they can focus their time and energy on</span>
  <span class="line">running their businesses.</span>
</p>

<section class="abs form-band"></section>
<h3 class="abs form-title">Request Information</h3>

<div class="abs field left" style="top:1897px">First Name</div>
<div class="abs field right" style="top:1897px">Last Name</div>
<div class="abs field left" style="top:1969px">Company Name</div>
<div class="abs field right" style="top:1969px">Phone Number</div>
<div class="abs field left" style="top:2041px">Email</div>
<div class="abs field right" style="top:2041px">Property Interested In</div>
<div class="abs field left" style="top:2113px">Product Interested In</div>
<div class="abs field right" style="top:2113px">Request a Tour</div>
<div class="abs field left" style="top:2185px">Number Of People</div>
<div class="abs field right" style="top:2185px">Move-In Date</div>

<div class="abs submit-btn">Submit</div>

<footer>
  <div class="abs footer-legal">COPYRIGHTS 2016<br>Calloway Business Centres</div>
  <span class="abs footer-link" style="left:653px">About</span>
  <span class="abs footer-link" style="left:715px">Contact</span>
  <span class="abs footer-link" style="left:785px">FAQ's</span>
  <span class="abs footer-link" style="left:848px">Careers</span>
</footer>

</body>
</html>
```